2 page PSD web design

I need a fairly simple website design built in PSD format for a site / blog in the finance niche. My current web address is www.velmarquest.com. Velmar Quest Hub is a site that teaches people how to trade options with a focus on income strategies.

I need a simple homepage built and then another similar template for all other pages including blog posts.

The rough design layout is shown attached excel file. It is similar to www.dorentakessly.com although I don't like the colors on his site at all. My logo is attached also, so the colours should be aligned with my logo.

In the header section, I will be giving away a free ebook called "No-Fluff Manual for Calendar Spreads" so I will need a 2D and 3D book cover designed as well. The design should be aligned with my logo and site design.

Industry/Entity Type

Finance

Requirements
Must have
• Everything is detailed in the excel file, but here is a list of must have items:

My current logo
ebook design and sign up section
under the ebook sign up section, need a big bold heading - "HELPING YOU TRADE IRON CONDORS AND OTHER INCOME STRATEGIES WITHOUT THE BS"
6 sidebar sections as detailed in excel file
Social Proof at top right, on the same line / level as the logo
"home advertise contact" in the top left in small discreet font
Should not have
• Do not want any photos or images on either of the pages

```html
<!DOCTYPE html>
<html lang="en">
<head>
<meta charset="utf-8">
<title>Velmar Quest Hub — Income Strategies</title>
<link rel="stylesheet" href="https://fonts.googleapis.com/css2?family=Arvo:wght@700&family=Cabin:wght@400;500;600;700&family=Questrial&family=Open+Sans:wght@400;600;700&display=swap">
<style>
:root{
  --blue-deep:#2a5a8e;
  --blue-mid:#3e73ad;
  --blue-bright:#2a83d1;
  --blue-text:#1d6fb8;
  --orange:#f07a1a;
  --orange-dark:#d9620a;
  --grey-panel:#d6d9dc;
  --grey-page:#f1f2f3;
  --ink:#2b2b2b;
  --ink-soft:#444;
  --meta:#2a78c2;
  --red:#c9141b;
  --footer:#3b3b3b;
  --white:#fff;
}
*{box-sizing:border-box;margin:0;padding:0}
html,body{width:838px;height:1200px;overflow:hidden}
body{position:relative;background:var(--grey-page);font-family:Arial,Helvetica,sans-serif;color:var(--ink)}
.abs{position:absolute}

/* top utility bar */
.utility{left:0;top:0;width:838px;height:22px;background:linear-gradient(#f4f4f4,#dcdcdc);border-bottom:1px solid #b9c4cf}
.utility nav{position:absolute;left:116px;top:5px;font:500 9px "Cabin",sans-serif;color:#1f3f66}
.utility nav span{margin:0 5px;color:#555}

/* header band */
.masthead{left:0;top:22px;width:838px;height:183px;background:linear-gradient(#3a6ea4 0%,#2f5f93 45%,#2b5a8c 100%)}
.masthead::after{content:"";position:absolute;left:0;top:90px;width:100%;height:1px;background:rgba(255,255,255,.12)}
.brand{left:100px;top:50px;display:flex;align-items:center;gap:10px}
.brand .dot{width:46px;height:46px;border-radius:50%;background:#5fa8e6}
.brand .name{font:600 24px "Cabin",sans-serif;color:#8fc6f2}
.social-proof{right:126px;top:41px;font:400 11px "Cabin",sans-serif;color:#fff}
.social-proof b{font-weight:700}
.social{left:552px;top:65px;display:flex;gap:6px}
.social i{display:block;width:34px;height:34px;border-radius:50%;background:#e9eef4;border:2px solid #1f4b7a}

.mainnav{left:116px;top:105px;height:40px;display:flex;align-items:center;font:600 9px "Open Sans",sans-serif;color:#fff}
.mainnav a{padding:0 14px;border-right:1px solid rgba(255,255,255,.18);color:#fff;text-decoration:none}
.mainnav a:last-child{border:none}
.mainnav a.active{background:linear-gradient(#fff,#dfe3e7);color:var(--blue-text);height:38px;line-height:38px;border-radius:4px 4px 0 0;padding:0 6px;margin-right:8px;border:none}

/* hero */
.hero{left:95px;top:150px;width:648px;height:180px;border-radius:10px;background:linear-gradient(#dfe1e3,#c9cccf);border:1px solid #b4b8bc}
.hero h1{position:absolute;left:22px;top:28px;font:700 20px "Arvo",serif;color:#3c3c3c;line-height:33px;white-space:nowrap}
.hero h1 em{font:italic 600 14px "Cabin",sans-serif;color:#333}
.hero .sub{position:absolute;left:17px;top:88px;font:400 19px "Questrial",sans-serif;color:var(--orange);white-space:nowrap}
.hero .sub small{font:600 11px "Cabin",sans-serif;color:#333}
.hero .sub span{color:var(--blue-bright)}
.hero p{position:absolute;left:27px;top:122px;width:360px;font:400 8.5px/16px "Open Sans",sans-serif;color:#333}
.cta-wrap{position:absolute;left:487px;top:55px;width:136px;height:62px;border-radius:6px;background:#e3e5e7;border:1px solid #c5c8cb}
.cta{position:absolute;left:9px;top:10px;width:118px;height:42px;border-radius:4px;background:linear-gradient(#f59a3a,var(--orange-dark));color:#fff;text-align:center;font:500 12px "Cabin",sans-serif;padding-top:6px}
.cta small{display:block;font:400 7.5px "Open Sans",sans-serif}
.dots{left:408px;top:330px;width:60px;height:16px;border-radius:0 0 30px 30px;background:#d0d3d6;display:flex;gap:3px;justify-content:center;padding-top:2px}
.dots i{width:8px;height:8px;border-radius:50%;background:#fff}
.dots i:first-child{background:var(--orange)}

.tagline{left:103px;top:354px;width:621px;height:36px;background:#fff;border:1px solid #d6d6d6;border-left:3px solid #444;border-right:3px solid #444;border-radius:6px;text-align:center;font:400 17px/34px "Questrial",sans-serif;color:#333}
.tagline span{color:var(--blue-text)}
.tagline b{font-weight:400;color:var(--orange)}

/* main column */
.section-bar{left:108px;width:401px;height:24px;border-radius:4px;background:linear-gradient(#6fb0ea,#2d7ccb);color:#fff;font:500 14px/24px "Cabin",sans-serif;padding-left:7px}
.post-title{left:110px;font:500 16px "Cabin",sans-serif;color:#222;white-space:nowrap}
.meta{left:112px;font:400 7px "Open Sans",sans-serif;color:var(--meta)}
.meta span{color:#333;margin-left:8px}
.thumb{left:109px;width:94px;height:80px;background:#fff;box-shadow:0 3px 3px rgba(0,0,0,.3);display:flex;align-items:center;justify-content:center;font:700 15px "Cabin",sans-serif;color:#111}
.thumb.photo{background:linear-gradient(#4a4a4a,#1f1f1f)}
.excerpt{left:211px;width:295px;font:400 7.6px/10.8px Arial,sans-serif;color:#333;text-align:justify}
.excerpt p{margin-bottom:4px}
.excerpt p + p + p{margin-top:3px}
.actions{left:348px;display:flex;gap:6px;align-items:center}
.btn{height:13px;padding:0 5px;border-radius:2px;font:italic 700 6.5px/13px Arial,sans-serif;color:#fff}
.btn.read{background:linear-gradient(#6fb0ea,#2d7ccb)}
.btn.share{background:#3b5a97;font-style:normal;width:40px;text-align:center}
.btn.post{background:none;color:var(--blue-bright);font:400 8px/13px Arial,sans-serif}
.divider{left:108px;width:402px;height:0;border-top:2px dotted #c8c8c8}

/* sidebar */
.card{left:547px;width:160px;background:#fff;border:1px solid #dadada;text-align:center}
.card h3{font:500 24px "Cabin",sans-serif;color:#222}
.card h4{font:500 15px "Cabin",sans-serif;color:var(--blue-text);margin-top:-3px}
.card p{font:400 8.5px/13px "Open Sans",sans-serif;color:#333}
.card .click{display:inline-block;margin-top:4px;width:75px;height:16px;background:var(--red);border-radius:2px;color:#fff;font:700 9px/16px Arial,sans-serif}
.side-head{left:549px;width:157px;height:23px;border-radius:3px;background:linear-gradient(#4a4a4a,#1c1c1c);color:#fff;font:500 12px/23px "Cabin",sans-serif;padding-left:7px}
.training{left:553px;top:620px;width:150px}
.training li{list-style:none;display:flex;align-items:center;gap:8px;height:31px;font:700 8px "Open Sans",sans-serif;color:#222}
.training li i{width:26px;height:24px;background:linear-gradient(#6a5b4d,#2e2a27)}
.sponsors{left:550px;top:789px;width:156px;display:grid;grid-template-columns:1fr 1fr;gap:4px}
.sponsors div{height:40px;background:#fff;border:1px solid #e1e1e1;display:flex;align-items:center;justify-content:center;font:700 11px "Cabin",sans-serif}
.kids{left:548px;top:893px;width:160px;height:111px;background:linear-gradient(90deg,#fff 0%,#fff 58%,#e0a860 80%,#8a5a2a 100%)}
.kids .name{position:absolute;left:9px;top:6px;font:700 16px "Cabin",sans-serif;color:#1d8ad6;line-height:18px}
.kids .name small{display:block;font:400 9px "Cabin",sans-serif;color:#1d6fb8}
.kids .strip{position:absolute;left:0;top:48px;width:106px;height:32px;background:#2a5f9c;color:#fff;font:600 7px/9px "Open Sans",sans-serif;padding:3px 10px}
.kids .give{position:absolute;left:0;bottom:0;width:160px;height:31px;background:#2e7cc9;color:#fff;font:600 9.5px/12px "Open Sans",sans-serif;padding:4px 9px}
.kids .give b{font-size:12px}
.subscribe{left:551px;top:1025px;width:162px;height:74px;background:#fff;border:1px solid #dadada;padding:6px 9px;font:400 8.5px/13px "Cabin",sans-serif;color:#333}
.subscribe span{font-size:13px;color:var(--blue-text)}
.subscribe .row{display:flex;justify-content:space-between;font-weight:600;margin-top:2px;padding-right:4px}

/* footer */
.footer{left:0;top:1146px;width:838px;height:54px;background:var(--footer)}
.footer nav{position:absolute;left:106px;top:17px;font:400 7.5px Arial,sans-serif;color:#ddd}
.footer nav span{margin:0 6px}
.footer .copy{position:absolute;left:106px;top:32px;font:400 7.5px Arial,sans-serif;color:#ddd}
.footer .brand-foot{position:absolute;left:570px;top:16px;display:flex;align-items:center;gap:7px}
.footer .brand-foot i{width:24px;height:24px;border-radius:50%;background:#9a9a9a}
.footer .brand-foot span{font:600 13px "Cabin",sans-serif;color:#a8a8a8}
</style>
</head>
<body>

<header class="abs utility">
  <nav>Home<span>|</span>Advertise<span>|</span>Contact</nav>
</header>

<section class="abs masthead"></section>
<div class="abs brand"><i class="dot"></i><span class="name">Velmar Quest Hub</span></div>
<div class="abs social-proof">Join a Community of <b>4279 AWESOME READERS</b></div>
<div class="abs social" aria-label="Social profiles"><i></i><i></i><i></i><i></i></div>

<nav class="abs mainnav">
  <a class="active">Articles and Videos</a><a>Trading Philosophy</a><a>Learning Centre</a><a>Free Tools</a><a>Members Only</a><a>Work With Us</a><a>About</a>
</nav>

<section class="abs hero">
  <h1>Do You Want To Know The Truth<br>About Iron Condors? <em>Learn How To Trade This</em></h1>
  <div class="sub">Amazing Option Income Strategy <small>With</small> <span>My FREE Ebook</span></div>
  <p>I will share with you my blueprint and all my tips and tricks for generating consistent monthly income with iron condors</p>
  <div class="cta-wrap"><div class="cta">INSTANT ACCESS<small>click here and get it now</small></div></div>
</section>
<div class="abs dots"><i></i><i></i><i></i><i></i></div>

<div class="abs tagline">Helping You <span>Trade Iron Condors</span> and Other Income Strategies without the <b>BS</b></div>

<!-- latest posts -->
<div class="abs section-bar" style="top:412px">Latest Posts</div>

<h2 class="abs post-title" style="top:443px">The Ultimate Guide to Double Diagonal Spreads</h2>
<div class="abs meta" style="top:467px">Posted by Reed Halvorsen.<span>|&nbsp;&nbsp; 2 Comments</span></div>
<div class="abs thumb photo" style="top:487px" role="img" aria-label="Author portrait photo"></div>
<div class="abs excerpt" style="top:484px">
  <p>Here is a brief exercise that I used in teaching nonverbal communication and that I rewrote for a textbook in nonverbal that I'm in the process of writing. Here I use it as an introduction to the discussion of height but it</p>
  <p>Business Communication Headline News: Find out what's going on in the world of corporate and business communications.</p>
  <p>Communication Overtones: Learn about using communications to better communicate within your organization, and with others outside your organization. Ledger Lens: This blog is meant for corporate communications professionals.</p>
</div>
<div class="abs actions" style="top:585px"><span class="btn read">Continue Reading</span><span class="btn share">SHARE</span><span class="btn post">Post</span></div>
<div class="abs divider" style="top:609px"></div>

<h2 class="abs post-title" style="top:620px">How To Protect Iron Condors From a Flash Crash</h2>
<div class="abs meta" style="top:644px">Posted by Reed Halvorsen.<span>|&nbsp;&nbsp; 2 Comments</span></div>
<div class="abs thumb" style="top:660px">Brightmart</div>
<div class="abs excerpt" style="top:657px">
  <p>Here is a brief exercise that I used in teaching nonverbal communication and that I rewrote for a textbook in nonverbal that I'm in the process of writing. Here I use it as an introduction to the discussion of height but it</p>
  <p>Business Communication Headline News: Find out what's going on in the world of corporate and business communications.</p>
  <p>Communication Overtones: Learn about using communications to better communicate within your organization, and with others outside your organization. Ledger Lens: This blog is meant for corporate communications professionals.</p>
</div>
<div class="abs actions" style="top:762px"><span class="btn read">Continue Reading</span><span class="btn share">SHARE</span><span class="btn post">Post</span></div>

<!-- featured posts -->
<div class="abs section-bar" style="top:794px">Featured Posts</div>

<h2 class="abs post-title" style="top:834px">How To Protect Iron Condors From a Flash Crash</h2>
<div class="abs meta" style="top:858px">Posted by Reed Halvorsen.<span>|&nbsp;&nbsp; 2 Comments</span></div>
<div class="abs thumb" style="top:876px;height:70px">Brightmart</div>
<div class="abs excerpt" style="top:880px">
  <p>Business Communication Headline News: Find out what's going on in the world of corporate and business communications.</p>
  <p>Communication Overtones: Learn about using communications to better communicate within your organization, and with others outside your organization. Ledger Lens: This blog is meant for corporate communications professionals.</p>
</div>
<div class="abs actions" style="top:949px"><span class="btn read">Continue Reading</span><span class="btn share">SHARE</span><span class="btn post">Post</span></div>
<div class="abs divider" style="top:975px"></div>

<h2 class="abs post-title" style="top:989px">How To Protect Iron Condors From a Flash Crash</h2>
<div class="abs meta" style="top:1013px">Posted by Reed Halvorsen.<span>|&nbsp;&nbsp; 2 Comments</span></div>
<div class="abs thumb" style="top:1031px;height:70px">Brightmart</div>
<div class="abs excerpt" style="top:1035px">
  <p>Business Communication Headline News: Find out what's going on in the world of corporate and business communications.</p>
  <p>Communication Overtones: Learn about using communications to better communicate within your organization, and with others outside your organization. Ledger Lens: This blog is meant for corporate communications professionals.</p>
</div>
<div class="abs actions" style="top:1104px"><span class="btn read">Continue Reading</span><span class="btn share">SHARE</span><span class="btn post">Post</span></div>

<!-- sidebar -->
<aside class="abs card" style="top:412px;height:100px;padding-top:3px">
  <h3>Work with us</h3>
  <h4>One-one-one</h4>
  <p>We're ready to help you achieve<br>the success you're looking for</p>
  <span class="click">CLICK HERE</span>
</aside>
<aside class="abs card" style="top:521px;height:62px;padding-top:2px">
  <h3 style="font-size:20px">New to Options?</h3>
  <p style="margin-top:4px">Check out our comprehensive<br>Training program</p>
</aside>

<div class="abs side-head" style="top:594px">Free Training</div>
<ul class="abs training">
  <li><i role="img" aria-label="Volatility tutorial thumbnail"></i>Volatility Tutorials</li>
  <li><i role="img" aria-label="Iron condor tutorial thumbnail"></i>Iron Condor Tutorials</li>
  <li><i role="img" aria-label="Income trading tutorial thumbnail"></i>Income Trading Tutorials</li>
  <li><i role="img" aria-label="Tools and resources thumbnail"></i>Free Tools and Resources</li>
</ul>

<div class="abs side-head" style="top:759px">Top Sponsors</div>
<div class="abs sponsors">
  <div style="color:#c9141b">Kestrel Credit</div>
  <div style="color:#1d4f8c">Harnwick</div>
  <div style="color:#1d3f8c">Cordaro</div>
  <div style="color:#c9141b">Quellis</div>
</div>

<div class="abs kids">
  <div class="name">BrightPath<small>KIDS FUND</small></div>
  <div class="abs" style="left:100px;top:0;width:60px;height:80px" role="img" aria-label="Photo of a parent and child"></div>
  <div class="strip">Together we will make a difference in the lives of children</div>
  <div class="give">Give Back to the Community<br>with <b>Corvanet</b></div>
</div>

<div class="abs subscribe">
  <span>Stay up</span> to date with Velmar Quest Hub. New articles and tutorials delivered straight to
  <div class="row"><span style="font-size:8.5px;color:#333">Email address:</span><span style="font-size:8.5px;color:#333">Let's Do This</span></div>
</div>

<footer class="abs footer">
  <nav>Articles and Videos<span>|</span>Trading Philosophy<span>|</span>Learning Centre<span>|</span>Free Tools<span>|</span>Members Only<span>|</span>Work With Us<span>|</span>About</nav>
  <div class="copy">Copyright © Velmar Quest Hub</div>
  <div class="brand-foot"><i></i><span>Velmar Quest Hub</span></div>
</footer>

</body>
</html>
```